Update Financial Planning Presentation

We currently use a stock Powerpoint template. Information is imputed into an Excel spreadsheet and then linked to the presentation. We are looking to improve and upgrade this to a more straightforward and "cleaner" looking template. I have attached a sample copy of the Powerpoint presantation we currently use along with the Excel spreadsheet. I have attached our logo as well. Thanks.
Industry/Entity Type
Financial

```html
<!DOCTYPE html>
<html lang="en">
<head>
<meta charset="utf-8">
<title>Harbor Lane – Presentation Template</title>
<link href="https://fonts.googleapis.com/css2?family=Open+Sans:wght@300;400;600;700&display=swap" rel="stylesheet">
<style>
:root{
  --green:#4a9a4f;
  --green-dark:#3c8a42;
  --ink:#1b1b1b;
  --text:#2a2a2a;
  --rule:#d9d9d9;
  --board:#d3d3d3;
  --paper:#ffffff;
}
*{box-sizing:border-box;margin:0;padding:0}
html,body{width:1200px;height:783px;overflow:hidden}
body{background:var(--board);font-family:"Open Sans",Arial,sans-serif;color:var(--text);position:relative}

.slide{position:absolute;width:380px;height:239px;background:var(--paper);overflow:hidden;box-shadow:0 1px 3px rgba(0,0,0,.25)}
.col-1{left:12px}.col-2{left:407px}.col-3{left:803px}
.row-1{top:17px}.row-2{top:273px}.row-3{top:531px}

/* brand name */
.brand{position:absolute;display:flex;align-items:center;gap:4px;white-space:nowrap;line-height:1}
.brand-square{width:6px;height:6px;background:var(--ink)}
.brand-name{font-weight:700;font-size:10px;color:var(--green-dark)}
.brand-center{left:50%;transform:translateX(-50%)}

.page-num{position:absolute;left:50%;bottom:10px;width:6px;height:6px;margin-left:-3px;border:0.6px solid #555;border-radius:50%}

/* headings */
.heading-plain{position:absolute;left:26px;top:26px;font-size:7.5px;color:var(--green);letter-spacing:.3px}
.heading-plain::after{content:"";position:absolute;left:0;top:13px;width:245px;height:0.5px;background:var(--rule)}
.heading-bar{position:absolute;top:22px;height:11px;font-size:7px;line-height:11px;padding-left:10px;letter-spacing:.3px}
.bar-black{background:var(--ink);color:var(--green)}
.bar-green{background:var(--green);color:#fff}
.bar-cap{position:absolute;top:22px;width:9px;height:11px}
.cap-green{background:var(--green)}
.cap-black{background:var(--ink)}
.band-top{position:absolute;left:0;top:0;width:100%;height:6px;background:var(--green)}

/* body copy */
.copy{position:absolute}
.copy .accent{color:var(--green)}
.copy-sm{font-size:3.9px;line-height:8.2px}
.copy-md{font-size:4.5px;line-height:9.4px}
.copy-lg{font-size:5.4px;line-height:8.8px}
.copy-divider{height:0.5px;background:var(--rule);margin:5px 0 6px}

/* title slide */
.title-rule-left{position:absolute;left:0;top:120px;width:23px;height:1.5px;background:var(--green)}
.title-rule-right{position:absolute;right:0;top:120px;width:26px;height:1.5px;background:var(--ink)}
.title-divider{position:absolute;left:175px;top:112px;width:1px;height:16px;background:var(--green)}
.title-text{position:absolute;left:195px;top:111px;font-weight:300;font-size:14px;color:var(--green);letter-spacing:.2px}

.thin-rule{position:absolute;height:0.5px;background:var(--rule)}
.v-rule{position:absolute;width:0.5px;background:var(--rule)}
</style>
</head>
<body>

<!-- 1: title -->
<section class="slide col-1 row-1">
  <div class="title-rule-left"></div>
  <div class="brand" style="left:72px;top:115px"><span class="brand-name">Harbor Lane</span><span class="brand-square"></span></div>
  <div class="title-divider"></div>
  <div class="title-text">TITLE GOES HERE</div>
  <div class="title-rule-right"></div>
</section>

<!-- 2: plain heading -->
<section class="slide col-2 row-1">
  <div class="heading-plain">HEADING</div>
  <div class="copy copy-md" style="left:26px;top:48px;width:250px">
    <p>Lorem ipsum dolor sit amet, consectetur adipiscing elit, sed do eiusmod tempor incididunt ut labore et dolore magna aliqua. Ut enim ad minim veniam, quis nostrud exercitation ullamco laboris nisi ut aliquip ex ea commodo consequat. Duis aute irure dolor in reprehenderit.</p>
    <p>Excepteur sint occaecat cupidatat non proident, sunt in culpa qui officia deserunt mollit anim id est laborum. Sed ut perspiciatis unde omnis iste natus error sit voluptatem accusantium doloremque laudantium.</p>
    <p>Beatae vitae dicta sunt explicabo. Nemo enim ipsam voluptatem quia voluptas sit aspernatur aut odit aut fugit, sed quia consequuntur magni dolores eos qui ratione voluptatem sequi nesciunt.</p>
    <p>Lorem ipsum dolor sit amet, consectetur adipiscing elit, sed do eiusmod tempor incididunt ut labore et dolore magna aliqua. Ut enim ad minim veniam, quis nostrud exercitation ullamco laboris nisi ut aliquip ex ea commodo consequat. Duis aute irure dolor in reprehenderit.</p>
    <p>Excepteur sint occaecat cupidatat non proident, sunt in culpa qui officia deserunt mollit anim id est laborum. Sed ut perspiciatis unde omnis iste natus error sit voluptatem accusantium doloremque laudantium.</p>
    <p>Beatae vitae dicta sunt explicabo. Nemo enim ipsam voluptatem quia voluptas sit aspernatur aut odit aut fugit, sed quia consequuntur magni dolores eos qui ratione voluptatem sequi nesciunt.</p>
  </div>
  <div class="brand" style="right:14px;bottom:14px"><span class="brand-name">Harbor Lane</span><span class="brand-square"></span></div>
  <div class="page-num"></div>
</section>

<!-- 3: black bar heading -->
<section class="slide col-3 row-1">
  <div class="heading-bar bar-black" style="left:17px;width:352px">HEADING</div>
  <div class="bar-cap cap-green" style="left:360px"></div>
  <div class="brand" style="right:14px;bottom:14px"><span class="brand-name">Harbor Lane</span><span class="brand-square"></span></div>
  <div class="page-num"></div>
</section>

<!-- 4: two columns, black bar -->
<section class="slide col-1 row-2">
  <div class="heading-bar bar-black" style="left:17px;width:352px">HEADING</div>
  <div class="bar-cap cap-green" style="left:360px"></div>
  <div class="copy copy-sm" style="left:20px;top:42px;width:170px">
    <p>Lorem ipsum dolor sit amet, consectetur adipiscing elit, sed do eiusmod tempor incididunt ut labore et dolore magna aliqua. Ut enim ad minim veniam, quis nostrud exercitation ullamco laboris nisi ut aliquip ex ea commodo consequat. Duis aute irure dolor in reprehenderit.</p>
    <p>Beatae vitae dicta sunt explicabo. Nemo enim ipsam voluptatem quia voluptas sit aspernatur aut odit aut fugit, sed quia consequuntur magni dolores eos qui ratione voluptatem sequi nesciunt.</p>
    <p>Excepteur sint occaecat cupidatat non proident, sunt in culpa qui officia deserunt mollit anim id est laborum. Sed ut perspiciatis unde omnis iste natus error sit voluptatem accusantium doloremque laudantium.</p>
    <p>Lorem ipsum dolor sit amet, consectetur adipiscing elit, sed do eiusmod tempor incididunt ut labore et dolore magna aliqua. Ut enim ad minim veniam, quis nostrud exercitation ullamco laboris nisi ut aliquip ex ea commodo consequat. Duis aute irure dolor in reprehenderit.</p>
    <p>Beatae vitae dicta sunt explicabo. Nemo enim ipsam voluptatem quia voluptas sit aspernatur aut odit aut fugit, sed quia consequuntur magni dolores eos qui ratione voluptatem sequi nesciunt.</p>
    <p>Excepteur sint occaecat cupidatat non proident, sunt in culpa qui officia deserunt mollit anim id est laborum. Sed ut perspiciatis unde omnis iste natus error sit voluptatem accusantium doloremque laudantium.</p>
  </div>
  <div class="copy copy-sm" style="left:198px;top:42px;width:170px">
    <p>Lorem ipsum dolor sit amet, consectetur adipiscing elit, sed do eiusmod tempor incididunt ut labore et dolore magna aliqua. Ut enim ad minim veniam, quis nostrud exercitation ullamco laboris nisi ut aliquip ex ea commodo consequat. Duis aute irure dolor in reprehenderit.</p>
    <p>Beatae vitae dicta sunt explicabo. Nemo enim ipsam voluptatem quia voluptas sit aspernatur aut odit aut fugit, sed quia consequuntur magni dolores eos qui ratione voluptatem sequi nesciunt.</p>
    <p>Excepteur sint occaecat cupidatat non proident, sunt in culpa qui officia deserunt mollit anim id est laborum. Sed ut perspiciatis unde omnis iste natus error sit voluptatem accusantium doloremque laudantium.</p>
    <p>Lorem ipsum dolor sit amet, consectetur adipiscing elit, sed do eiusmod tempor incididunt ut labore et dolore magna aliqua. Ut enim ad minim veniam, quis nostrud exercitation ullamco laboris nisi ut aliquip ex ea commodo consequat. Duis aute irure dolor in reprehenderit.</p>
    <p>Beatae vitae dicta sunt explicabo. Nemo enim ipsam voluptatem quia voluptas sit aspernatur aut odit aut fugit, sed quia consequuntur magni dolores eos qui ratione voluptatem sequi nesciunt.</p>
    <p>Excepteur sint occaecat cupidatat non proident, sunt in culpa qui officia deserunt mollit anim id est laborum. Sed ut perspiciatis unde omnis iste natus error sit voluptatem accusantium doloremque laudantium.</p>
  </div>
  <div class="brand" style="right:14px;bottom:12px"><span class="brand-name">Harbor Lane</span><span class="brand-square"></span></div>
  <div class="page-num"></div>
</section>

<!-- 5: two columns, green bar -->
<section class="slide col-2 row-2">
  <div class="heading-bar bar-green" style="left:17px;width:352px">HEADING</div>
  <div class="bar-cap cap-black" style="left:360px"></div>
  <div class="copy copy-sm" style="left:20px;top:42px;width:170px">
    <p>Lorem ipsum dolor sit amet, consectetur adipiscing elit, sed do eiusmod tempor incididunt ut labore et dolore magna aliqua. Ut enim ad minim veniam, quis nostrud exercitation ullamco laboris nisi ut aliquip ex ea commodo consequat. Duis aute irure dolor in reprehenderit.</p>
    <p>Beatae vitae dicta sunt explicabo. Nemo enim ipsam voluptatem quia voluptas sit aspernatur aut odit aut fugit, sed quia consequuntur magni dolores eos qui ratione voluptatem sequi nesciunt.</p>
    <p>Excepteur sint occaecat cupidatat non proident, sunt in culpa qui officia deserunt mollit anim id est laborum. Sed ut perspiciatis unde omnis iste natus error sit voluptatem accusantium doloremque laudantium.</p>
    <p>Lorem ipsum dolor sit amet, consectetur adipiscing elit, sed do eiusmod tempor incididunt ut labore et dolore magna aliqua. Ut enim ad minim veniam, quis nostrud exercitation ullamco laboris nisi ut aliquip ex ea commodo consequat. Duis aute irure dolor in reprehenderit.</p>
    <p>Beatae vitae dicta sunt explicabo. Nemo enim ipsam voluptatem quia voluptas sit aspernatur aut odit aut fugit, sed quia consequuntur magni dolores eos qui ratione voluptatem sequi nesciunt.</p>
    <p>Excepteur sint occaecat cupidatat non proident, sunt in culpa qui officia deserunt mollit anim id est laborum. Sed ut perspiciatis unde omnis iste natus error sit voluptatem accusantium doloremque laudantium.</p>
  </div>
  <div class="copy copy-sm" style="left:198px;top:42px;width:170px">
    <p>Lorem ipsum dolor sit amet, consectetur adipiscing elit, sed do eiusmod tempor incididunt ut labore et dolore magna aliqua. Ut enim ad minim veniam, quis nostrud exercitation ullamco laboris nisi ut aliquip ex ea commodo consequat. Duis aute irure dolor in reprehenderit.</p>
    <p>Excepteur sint occaecat cupidatat non proident, sunt in culpa qui officia deserunt mollit anim id est laborum. Sed ut perspiciatis unde omnis iste natus error sit voluptatem accusantium doloremque laudantium.</p>
    <p class="accent">Beatae vitae dicta sunt explicabo. Nemo enim ipsam voluptatem quia voluptas sit aspernatur aut odit aut fugit, sed quia consequuntur magni dolores eos qui ratione voluptatem sequi nesciunt.</p>
    <p>Lorem ipsum dolor sit amet, consectetur adipiscing elit, sed do eiusmod tempor incididunt ut labore et dolore magna aliqua. Ut enim ad minim veniam, quis nostrud exercitation ullamco laboris nisi ut aliquip ex ea commodo consequat. Duis aute irure dolor in reprehenderit.</p>
    <p>Beatae vitae dicta sunt explicabo. Nemo enim ipsam voluptatem quia voluptas sit aspernatur aut odit aut fugit, sed quia consequuntur magni dolores eos qui ratione voluptatem sequi nesciunt.</p>
    <p>Excepteur sint occaecat cupidatat non proident, sunt in culpa qui officia deserunt mollit anim id est laborum. Sed ut perspiciatis unde omnis iste natus error sit voluptatem accusantium doloremque laudantium.</p>
  </div>
  <div class="brand" style="right:14px;bottom:12px"><span class="brand-name">Harbor Lane</span><span class="brand-square"></span></div>
  <div class="page-num"></div>
</section>

<!-- 6: green bar with name top right -->
<section class="slide col-3 row-2">
  <div class="heading-bar bar-green" style="left:17px;width:258px">HEADING</div>
  <div class="brand" style="left:285px;top:23px"><span class="brand-name">Harbor Lane</span></div>
  <div class="bar-cap cap-black" style="left:364px;width:12px"></div>
  <div class="copy copy-lg" style="left:26px;top:50px;width:336px">
    <p>Lorem ipsum dolor sit amet, consectetur adipiscing elit, sed do eiusmod tempor incididunt ut labore et dolore magna aliqua. Ut enim ad minim veniam, quis nostrud exercitation ullamco laboris nisi ut aliquip ex ea commodo consequat. Duis aute irure dolor in reprehenderit.</p>
    <p class="accent">Beatae vitae dicta sunt explicabo. Nemo enim ipsam voluptatem quia voluptas sit aspernatur aut odit aut fugit, sed quia consequuntur magni dolores eos qui ratione voluptatem sequi nesciunt.</p>
    <p>Excepteur sint occaecat cupidatat non proident, sunt in culpa qui officia deserunt mollit anim id est laborum. Sed ut perspiciatis unde omnis iste natus error sit voluptatem accusantium doloremque laudantium. Duis aute irure dolor in reprehenderit in voluptate velit esse cillum dolore eu fugiat nulla pariatur.</p>
    <div class="copy-divider"></div>
    <p>Excepteur sint occaecat cupidatat non proident, sunt in culpa qui officia deserunt mollit anim id est laborum. Sed ut perspiciatis unde omnis iste natus error sit voluptatem accusantium doloremque laudantium.</p>
  </div>
  <div class="page-num"></div>
</section>

<!-- 7: top band, centered name, text -->
<section class="slide col-1 row-3">
  <div class="band-top"></div>
  <div class="brand brand-center" style="top:28px"><span class="brand-name">Harbor Lane</span><span class="brand-square"></span></div>
  <div class="copy copy-lg" style="left:26px;top:50px;width:336px">
    <p>Lorem ipsum dolor sit amet, consectetur adipiscing elit, sed do eiusmod tempor incididunt ut labore et dolore magna aliqua. Ut enim ad minim veniam, quis nostrud exercitation ullamco laboris nisi ut aliquip ex ea commodo consequat. Duis aute irure dolor in reprehenderit.</p>
    <p class="accent">Beatae vitae dicta sunt explicabo. Nemo enim ipsam voluptatem quia voluptas sit aspernatur aut odit aut fugit, sed quia consequuntur magni dolores eos qui ratione voluptatem sequi nesciunt.</p>
    <p>Excepteur sint occaecat cupidatat non proident, sunt in culpa qui officia deserunt mollit anim id est laborum. Sed ut perspiciatis unde omnis iste natus error sit voluptatem accusantium doloremque laudantium. Duis aute irure dolor in reprehenderit in voluptate velit esse cillum dolore eu fugiat nulla pariatur.</p>
    <div class="copy-divider"></div>
    <p>Excepteur sint occaecat cupidatat non proident, sunt in culpa qui officia deserunt mollit anim id est laborum. Sed ut perspiciatis unde omnis iste natus error sit voluptatem accusantium doloremque laudantium.</p>
  </div>
  <div class="page-num"></div>
</section>

<!-- 8: top band, centered name, empty -->
<section class="slide col-2 row-3">
  <div class="band-top"></div>
  <div class="brand brand-center" style="top:28px"><span class="brand-name">Harbor Lane</span><span class="brand-square"></span></div>
  <div class="thin-rule" style="left:36px;top:156px;width:308px"></div>
  <div class="page-num"></div>
</section>

<!-- 9: top band, name left, text right -->
<section class="slide col-3 row-3">
  <div class="band-top"></div>
  <div class="brand" style="left:30px;top:113px"><span class="brand-name">Harbor Lane</span><span class="brand-square"></span></div>
  <div class="v-rule" style="left:145px;top:40px;height:172px"></div>
  <div class="copy copy-lg" style="left:165px;top:28px;width:196px">
    <p>Lorem ipsum dolor sit amet, consectetur adipiscing elit, sed do eiusmod tempor incididunt ut labore et dolore magna aliqua. Ut enim ad minim veniam, quis nostrud exercitation ullamco laboris nisi ut aliquip ex ea commodo consequat. Duis aute irure dolor in reprehenderit.</p>
    <p class="accent">Beatae vitae dicta sunt explicabo. Nemo enim ipsam voluptatem quia voluptas sit aspernatur aut odit aut fugit, sed quia consequuntur magni dolores eos qui ratione voluptatem sequi nesciunt.</p>
    <p>Excepteur sint occaecat cupidatat non proident, sunt in culpa qui officia deserunt mollit anim id est laborum. Sed ut perspiciatis unde omnis iste natus error sit voluptatem accusantium doloremque laudantium.</p>
    <p>Duis aute irure dolor in reprehenderit in voluptate velit esse cillum dolore eu fugiat nulla pariatur. Ut enim ad minim veniam, quis nostrud exercitation ullamco laboris nisi ut aliquip.</p>
  </div>
  <div class="page-num"></div>
</section>

</body>
</html>
```